Family Farm Produce poster design

I have attached a ps file of a rough design i am after for a flow chart on our family farm and how people can buy our produce. I would like someone to tidy it up and make it look great. Using the same font (KG Second Chances Sket...) and similar photos (please message me for more photos if needed) . I am after a PS file of the design as details change from time to time .

Industry/Entity Type

Farm

```html
<!DOCTYPE html>
<html lang="en">
<head>
<meta charset="utf-8">
<title>Brookvale Produce – Family Farm Flyer</title>
<link rel="stylesheet" href="https://fonts.googleapis.com/css2?family=Patrick+Hand&family=Lato:wght@400;700&display=swap">
<style>
  :root{
    --bg:#3f4a52;
    --paper:#ffffff;
    --pink:#ee7676;
    --green:#62d56f;
    --lavender:#a7a3f0;
    --grey:#6a6a6a;
    --ink:#3a3a3a;
    --footer:#3b3b3d;
    --sky:#8fc3ee;
    --hill:#3f6e2f;
    --grass:#7fc94a;
  }
  *{margin:0;padding:0;box-sizing:border-box}
  html,body{width:1200px;height:1200px;overflow:hidden;background:var(--bg)}
  .flyer{position:absolute;left:180px;top:6px;width:840px;height:1187px;background:var(--paper);
    font-family:"Patrick Hand",cursive;color:var(--grey);overflow:hidden}
  .shapes{position:absolute;left:0;top:0}
  .brand{position:absolute;left:72px;top:26px;width:136px;height:136px;border-radius:50%;
    background:var(--pink);color:#fff;display:flex;flex-direction:column;align-items:center;justify-content:center;
    font-size:21px;line-height:1;letter-spacing:1px;text-align:center}
  .t{position:absolute;transform:translateX(-50%);text-align:center;white-space:nowrap;line-height:1.1}
  .title{color:var(--green);font-size:30px;line-height:1}
  .lead{font-size:20px}
  .sub{font-size:18px}
  .item{font-size:21px}
  .note{font-size:16px}
  .pink{color:var(--pink)} .green{color:var(--green)} .lav{color:var(--lavender)}
  .chart-line{fill:none;stroke:var(--grey);stroke-width:2}
  .list{position:absolute;list-style:none;font-size:15px;line-height:1}
  .list li{position:relative;padding-left:28px;margin-bottom:12px}
  .list svg{position:absolute;left:0;top:0;width:19px;height:19px}
  .list.online{left:40px;top:885px;width:240px;color:var(--lavender)}
  .list.club{left:304px;top:885px;width:290px;color:var(--grey)}
  .list.markets{left:618px;top:885px;width:190px;color:var(--pink)}
  .list.markets li{margin-bottom:16px}
  .footer{position:absolute;left:0;width:840px;color:#fff;font-family:"Lato",sans-serif;font-size:12.5px;text-align:center}
  .footer svg{width:13px;height:13px;vertical-align:-2px;margin-right:6px}
  .contacts{display:flex;justify-content:center;gap:24px}
</style>
</head>
<body>
<svg width="0" height="0" style="position:absolute">
  <symbol id="tick" viewBox="0 0 20 20"><circle cx="9" cy="11" r="7.5" fill="none" stroke="currentColor" stroke-width="1.8"/><path d="M5.5 10.5l3 3 9-10" fill="none" stroke="currentColor" stroke-width="1.8" stroke-linecap="round"/></symbol>
</svg>

<div class="flyer">
  <svg class="shapes" width="840" height="1187" viewBox="0 0 840 1187">
    <defs>
      <linearGradient id="scene" x1="0" y1="0" x2="0" y2="1">
        <stop offset="0" stop-color="var(--sky)"/>
        <stop offset="0.35" stop-color="#d9e9f5"/>
        <stop offset="0.5" stop-color="var(--hill)"/>
        <stop offset="0.7" stop-color="var(--grass)"/>
        <stop offset="1" stop-color="#5d9a3a"/>
      </linearGradient>
    </defs>
    <path d="M0 262 Q420 500 840 262 V300 Q420 512 0 300 Z" fill="var(--pink)"/>
    <path d="M0 0 H840 V262 Q420 499 0 262 Z" fill="url(#scene)" role="img" aria-label="Photo of visitors watching a herd of cattle grazing on green pasture below a forested hill"/>
    <path class="chart-line" d="M137 545 V523 H702 V545 M420 523 V545"/>
    <path class="chart-line" d="M137 665 V645 H702 V665 M420 645 V665"/>
    <path class="chart-line" d="M137 832 V812 H702 V832 M420 812 V832"/>
    <path d="M0 1187 Q420 940 840 1187 Z" fill="var(--pink)"/>
    <path d="M40 1187 Q420 965 800 1187 Z" fill="var(--footer)" stroke="#fff" stroke-width="3"/>
  </svg>

  <div class="brand">BROOKVALE<br>PRODUCE</div>

  <div class="t title" style="left:425px;top:410px">BROOKVALE PRODUCE<br>FAMILY FARM</div>
  <div class="t sub" style="left:140px;top:447px">Local</div>
  <div class="t sub" style="left:706px;top:444px">Healthy</div>

  <div class="t lead" style="left:425px;top:488px">How do we farm?</div>
  <div class="t item pink" style="left:140px;top:548px">Organic</div>
  <div class="t note" style="left:140px;top:573px">(chemical Free)</div>
  <div class="t item green" style="left:425px;top:548px">Nutirent Dense</div>
  <div class="t note green" style="left:425px;top:573px">(Add life to soil)</div>
  <div class="t item lav" style="left:706px;top:548px">pasture Raised</div>
  <div class="t note" style="left:706px;top:573px">(outdoors+ Moving)</div>

  <div class="t lead pink" style="left:425px;top:614px">What do we farm?</div>
  <div class="t sub pink" style="left:140px;top:670px">Beef</div>
  <div class="t sub" style="left:140px;top:692px">(100% grass fed)</div>
  <div class="t note" style="left:436px;top:671px;text-align:left;line-height:1.6">-Meal ready portions<br>-Buy only the cuts you want<br>-buy bulk and save</div>
  <div class="t sub lav" style="left:706px;top:670px">Eggs</div>
  <div class="t sub" style="left:706px;top:692px">(Fresh Delicious)</div>

  <div class="t sub" style="left:140px;top:756px">Quality<br>Guarenteed</div>
  <div class="t lead lav" style="left:420px;top:756px">How do I buy?</div>
  <div class="t sub" style="left:682px;top:756px">Follow us on social media<br>or visit the farm!</div>

  <div class="t note pink" style="left:140px;top:839px">Online</div>
  <div class="t note" style="left:420px;top:839px">Buying Club</div>
  <div class="t note lav" style="left:710px;top:839px;line-height:1">Farmers Markets<br>and retail stockists</div>

  <ul class="list online" style="--c:var(--ink)">
    <li><svg style="color:var(--ink)"><use href="#tick"/></svg>go to our website<br>www.brookvaleproduce.com.au</li>
    <li><svg style="color:var(--ink)"><use href="#tick"/></svg>chose what you want</li>
    <li><svg style="color:var(--ink)"><use href="#tick"/></svg>Process at check out</li>
    <li><svg style="color:var(--ink)"><use href="#tick"/></svg>it is then delivered<br>to your home or workplace<br>in cooler bags ready for<br>yoiu to refridgerate.</li>
  </ul>
  <ul class="list club">
    <li><svg style="color:var(--pink)"><use href="#tick"/></svg>go to our website<br>www.brookvaleproduce.com.au</li>
    <li><svg style="color:var(--pink)"><use href="#tick"/></svg>Choose what you want</li>
    <li><svg style="color:var(--pink)"><use href="#tick"/></svg>Quote buying club name</li>
    <li><svg style="color:var(--pink)"><use href="#tick"/></svg>Process at check out</li>
    <li><svg style="color:var(--pink)"><use href="#tick"/></svg>All orders in your buying club<br>are delivered to one location and<br>10% is donated back to your funraiser</li>
  </ul>
  <ul class="list markets">
    <li><svg style="color:var(--lavender)"><use href="#tick"/></svg>Seaside Markets<br>each sunday at the<br>Bay Jetty</li>
    <li><svg style="color:var(--lavender)"><use href="#tick"/></svg>Riverton Growers<br>market 2nd &amp; 4th<br>Saturday of the<br>month</li>
    <li><svg style="color:var(--lavender)"><use href="#tick"/></svg>Hesd to our website<br>for full stockists list.</li>
  </ul>

  <div class="footer" style="top:1103px;line-height:1.25">
    <svg viewBox="0 0 12 14"><path d="M6 13S1.5 8 1.5 5a4.5 4.5 0 0 1 9 0C10.5 8 6 13 6 13z" fill="none" stroke="var(--pink)" stroke-width="1.6"/><circle cx="6" cy="5" r="1.6" fill="var(--pink)"/></svg>42 millers gully road<br>Upper Ferndale, New South Wales, Australia
  </div>
  <div class="footer contacts" style="top:1146px">
    <span><svg viewBox="0 0 14 14"><path d="M3 1l2.5 3-1.5 1.5a8 8 0 0 0 4.5 4.5L10 8.5l3 2.5-1.5 2C6 13 1 8 1 2.5z" fill="none" stroke="var(--pink)" stroke-width="1.4"/></svg>61 400 555 019</span>
    <span><svg viewBox="0 0 14 14"><rect x="1" y="3" width="12" height="8" fill="var(--pink)"/><path d="M1 3l6 5 6-5" fill="none" stroke="var(--footer)" stroke-width="1.2"/></svg>hello@brookvaleproduce.com.au</span>
    <span><svg viewBox="0 0 14 14"><circle cx="7" cy="7" r="5.8" fill="none" stroke="var(--pink)" stroke-width="1.4"/><path d="M1.5 7h11M7 1.2c-3 3.5-3 8.1 0 11.6M7 1.2c3 3.5 3 8.1 0 11.6" fill="none" stroke="var(--pink)" stroke-width="1.1"/></svg>www.brookvaleaustralia.com.au</span>
  </div>
</div>
</body>
</html>
```